2 page Web Site Design (Coded), simple, not picky

I need a web portal for a PPC marketing business. I have the logo, some imagery, and some websites to base the design on.

***Background***
The name of the business is "Quiet Harbor Outreach Partners" or QHOP. We provide listings in a searchable database for Dental Sleep Medicine doctors. These are doctors who treat snoring/sleep apnea/and CPAP users with oral appliances. Client doctors will have their own "landing page website" where PPC prospects land from the PPC campaigns. Logos for supporting/landing page websites have been uploaded.
***End Background***

THIS website (for you to design) is to introduce doctors to the concept and detail the services. i.e. PPC campaign management services, listing on a national database of Dental Sleep Medicine practitioners, and a fully featured website dedicated to Snoring, Sleep Apnea, and CPAP Alternative treatment (those websites are "Farewell-Rumble.com", "Farewell-NightPause.com", and ""Farewell-MaskFree.com")

SEM websites whose look I enjoy are:

http://www.brivolta.com/marketing-services/pay-per-click/

http://www.quellandrift.com/welcome/pay-per-click-services/

http://www.tarnolux4co.com/marketing-services/paid-search-management/

The main colors are Red, White, & Blue. Red and blue used mostly for accents/emphasis.

The main/index page's purpose is to, as best possible, convey the idea of SEM campaign management with supporting websites being their best option for internet marketing!
The secondary page is just a slightly modified layout where details can be explained.

Target Market(s)

Dentists who practice Dental Sleep Medicine (see www.pqwrl.org)

Industry/Entity Type

Marketing

Requirements
Must have
• -Sign-up form for the generation of leads... Simple script that sends E-mail is fine... Doctor's Name, Business Name, Business Address, E-mail address, phone #.

-Graphics that will clearly describe the services being provided.

```html
<!DOCTYPE html>
<html lang="en">
<head>
<meta charset="utf-8">
<title>QHOP – Internet Marketing for Sleep Therapists</title>
<link href="https://fonts.googleapis.com/css2?family=PT+Sans:wght@400;700&family=PT+Sans+Narrow:wght@400;700&family=Ubuntu:wght@400&display=swap" rel="stylesheet">
<style>
:root{
  --red:#b3222e;
  --red-light:#c9404a;
  --blue:#5b67a6;
  --navy:#3f4f8f;
  --ink:#444;
  --muted:#888;
  --hero-bg:#ececec;
  --line:#dedede;
  --card-head:#f1f1f1;
  --dark:#545454;
  --white:#fff;
}
*{box-sizing:border-box;margin:0;padding:0}
html,body{width:1200px;height:1140px;overflow:hidden;background:var(--white)}
.page{position:relative;width:1400px;height:1330px;transform:scale(0.857143);transform-origin:0 0;font-family:"PT Sans",sans-serif;color:var(--ink)}
.abs{position:absolute}
.topbar{left:200px;top:0;width:1000px;height:12px;background:var(--dark)}
.brand{left:203px;top:36px;display:flex;align-items:center;gap:12px}
.brand-mark{width:56px;height:56px;border-radius:50%;background:var(--navy)}
.brand-name{font-family:"PT Sans",sans-serif;font-weight:700;color:var(--red);font-size:40px;line-height:40px;letter-spacing:1px}
.brand-tag{font-family:"PT Sans",sans-serif;font-weight:700;color:var(--red);font-size:12.5px;margin-top:4px}
.nav{right:200px;top:57px;display:flex;gap:28px;font-family:"PT Sans Narrow",sans-serif;font-size:16px;letter-spacing:1px;color:var(--muted)}
.nav .active{color:var(--red)}
.hero{left:0;top:120px;width:1400px;height:355px;background:var(--hero-bg)}
.hero h1{position:absolute;left:213px;top:150px;font-family:"Ubuntu",sans-serif;font-weight:400;font-size:37px;line-height:48px;color:#4a4a4a}
.hero h1 em{font-style:normal;color:var(--blue)}
.hero-text{left:213px;top:265px;width:520px;font-size:13px;line-height:26px;letter-spacing:1.1px}
.bullets{left:215px;top:339px;list-style:none}
.bullets li{font-size:11.5px;font-weight:700;letter-spacing:1px;color:var(--navy);height:34px;display:flex;gap:10px}
.bullets li::before{content:"";width:0;height:0;border-left:8px solid var(--red);border-top:5px solid transparent;border-bottom:5px solid transparent;margin-top:3px}
.hero-frame{left:746px;top:145px;width:454px;height:303px;background:var(--white);box-shadow:0 1px 3px rgba(0,0,0,.12)}
.hero-photo{left:760px;top:159px;width:426px;height:275px;background:linear-gradient(135deg,#e4e2e0,#cfc4b8 55%,#b8a898)}
.intro{left:214px;top:493px;width:645px;font-size:13px;line-height:30px;letter-spacing:1.1px}
.intro a{color:var(--red);text-decoration:none}
.cta{left:908px;top:517px;width:277px;height:63px;background:linear-gradient(var(--red-light) 50%,var(--red) 50%);color:var(--white);font-size:18px;letter-spacing:2.5px;display:flex;align-items:center;justify-content:center;font-weight:700}
.features{left:200px;top:633px;width:1001px;height:421px;border:1px solid var(--line)}
.card{top:666px;width:285px;height:356px;border:1px solid #e2e2e2;border-radius:4px;background:var(--white);box-shadow:0 1px 2px rgba(0,0,0,.06);overflow:hidden}
.card-head{height:44px;background:var(--card-head);display:flex;align-items:center;justify-content:center;gap:12px;font-size:15px;letter-spacing:.6px;color:#555}
.card p{padding:14px 17px 0;font-size:12.5px;line-height:22px;letter-spacing:.8px;color:#666}
.card-img{position:absolute;left:0;top:154px;width:100%;height:143px}
.more{position:absolute;top:310px;left:50%;transform:translateX(-50%);width:81px;height:31px;background:var(--red);color:var(--white);font-family:"PT Sans Narrow",sans-serif;font-size:15px;letter-spacing:1px;display:flex;align-items:center;justify-content:center}
.field{position:absolute;left:14px;width:256px;height:36px;border:1px solid #aab;border-radius:2px;padding-left:14px;display:flex;align-items:center;font-size:11px;font-style:italic;letter-spacing:1px;color:var(--navy)}
.sites{left:200px;top:1095px;width:1000px;height:140px;background:#efefef;border:1px solid var(--line);display:flex;align-items:center;justify-content:space-around}
.site{display:flex;align-items:center;gap:10px;font-weight:700;font-size:24px;color:var(--navy)}
.site i{width:44px;height:44px;border-radius:50%;background:var(--navy)}
.footer{left:0;top:1272px;width:1400px;height:58px;background:var(--dark)}
.footer-mark{left:200px;top:1285px;width:34px;height:34px;border-radius:50%;background:var(--navy)}
.copy{left:251px;top:1292px;font-size:11px;letter-spacing:.6px;color:#eee}
.footer-nav{right:200px;top:1292px;display:flex;gap:19px;font-size:11px;color:#eee}
.footer-nav .active{color:#e0555e}
</style>
</head>
<body>
<div class="page">
  <div class="abs topbar"></div>
  <div class="abs brand">
    <span class="brand-mark"></span>
    <div><div class="brand-name">QHOP LLC</div><div class="brand-tag">Quiet Harbor Outreach Partners</div></div>
  </div>
  <nav class="abs nav"><span class="active">HOME</span><span>SERVICES</span><span>CLIENTS</span><span>ABOUT</span><span>BLOG</span><span>CONTACT US</span></nav>

  <section class="abs hero"></section>
  <div class="hero" style="position:absolute;left:0;top:0;background:none;height:0">
    <h1><em>Effective &amp; affordable</em> internet<br>marketing for Sleep Therapists</h1>
  </div>
  <p class="abs hero-text">Ensure your sleep disorder practice is easily found and visited online by using our highly effective PPC and internet marketing methods</p>
  <ul class="abs bullets">
    <li>A fully featured website dedicated to Snoring, Sleep Apnea, and CPAP</li>
    <li>Listing on a national database of Dental Sleep Medicine practitioners</li>
    <li>PPC prospects consistently land from the PPC campaigns</li>
  </ul>
  <div class="abs hero-frame"></div>
  <div class="abs hero-photo" role="img" aria-label="Photo of an older couple shopping online at a laptop"></div>

  <p class="abs intro">When your business spends money on advertising, it can be difficult to know with certainty what the <a href="#">return on that investment</a> is. As a pay-per-click company, we have heard that frustration from marketing executives, and we are happy to be able to <a href="#">provide answers</a>. A well-researched pay-per-click ad campaign.</p>
  <div class="abs cta">FIND OUT MORE</div>

  <div class="abs features"></div>
  <article class="abs card" style="left:228px">
    <div class="card-head"><svg width="24" height="24" viewBox="0 0 24 24"><circle cx="12" cy="12" r="8" fill="none" stroke="#666" stroke-width="5" stroke-dasharray="3 2.2"/><circle cx="12" cy="12" r="6" fill="#666"/><circle cx="12" cy="12" r="2.5" fill="#f1f1f1"/></svg>LOREM IPSUM CENTARINOS</div>
    <p>Cras vel velit mauris. Proin et odio eu dui euismod congue eget et neque. Maecenas lectus magna, dignissim et varius vitae heetore.</p>
    <div class="card-img" role="img" aria-label="Photo of a hand pointing at charts on a monitor" style="background:linear-gradient(120deg,#4c5560,#cfd6e0 40%,#e8ecf2)"></div>
    <div class="more">MORE</div>
  </article>
  <article class="abs card" style="left:560px">
    <div class="card-head"><svg width="20" height="26" viewBox="0 0 20 26"><circle cx="10" cy="9" r="7" fill="none" stroke="#666" stroke-width="2.5"/><rect x="6" y="17" width="8" height="6" rx="1" fill="#666"/></svg>LOREM IPSUM DOLOMBER</div>
    <p>Cras vel velit mauris. Proin et odio eu dui euismod congue eget et neque. Maecenas lectus magna, dignissim et varius vitae heetore.</p>
    <div class="card-img" role="img" aria-label="Illustration of a monitor showing search results with pay per click ads highlighted" style="background:linear-gradient(#ececec,#d8d8d8)"></div>
    <div class="more">MORE</div>
  </article>
  <article class="abs card" style="left:888px">
    <div class="card-head"><svg width="26" height="26" viewBox="0 0 26 26"><circle cx="13" cy="8" r="6" fill="#666"/><path d="M1 26c0-8 5-11 12-11s12 3 12 11z" fill="#666"/></svg>SIGN UP TO OUR SERVICE</div>
    <p>Cras vel velit mauris. Proin et odio eu dui euismod congue eget et neque.</p>
    <div class="field" style="top:125px">Your Name</div>
    <div class="field" style="top:184px">Your Email</div>
    <div class="field" style="top:245px">Your Phone Number</div>
    <div class="more">MORE</div>
  </article>

  <div class="abs sites">
    <div class="site"><i></i>Farewell-Rumble.com</div>
    <div class="site"><i></i>Farewell-NightPause.com</div>
    <div class="site"><i></i>Farewell-MaskFree.com</div>
  </div>

  <footer class="abs footer"></footer>
  <div class="abs footer-mark"></div>
  <div class="abs copy">Copyright ©2012 Quiet Harbor Outreach Partners All rights reserved</div>
  <nav class="abs footer-nav"><span class="active">Home</span><span>Services</span><span>Clients</span><span>About</span><span>Blog</span><span>Contact Us</span></nav>
</div>
</body>
</html>
```